Business Card Design for general contractor or developer

General Contractors. We build new buildings as well as redesign and/or remodel existing buildings. Mostly residential, but we want to expand to commercial as well, so we want the design not to be residential specific.We want the design to be modern, but necessarily minimalistic. A monogram type is also a consideration, but would like to see all ideas.

Target Market(s)

Real estate investors, homeowners, future homeowners, commercial building owners

Industry/Entity Type

Contractor

Contact Information for Business Card

BRIMCOVE Developers Corp, 6127 NE 318th Avenue Suite 241 Miami Lakes, FL 33482, Curtis Ortega, (305) 472-1803, curtis@quarvinta.com

Font styles to use
Other font styles liked:
• Modern type font

Requirements
Must have
• Must be modern looking
Nice to have
• Metallic type or a standout feature
Should not have
• Tools, floorplans

```html
<!DOCTYPE html>
<html lang="en">
<head>
<meta charset="utf-8">
<title>Curtis Ortega — Business Card</title>
<link href="https://fonts.googleapis.com/css2?family=Open+Sans:wght@400;600&display=swap" rel="stylesheet">
<style>
  :root {
    --page: #ffffff;
    --card-dark: #1d2220;
    --ink-light: #ffffff;
    --name-box: #121414;
    --photo-top: #eef0ef;
    --photo-mid: #d9dcda;
    --photo-low: #6d716f;
  }
  html, body {
    margin: 0;
    padding: 0;
    width: 1200px;
    height: 720px;
    overflow: hidden;
    background: var(--page);
  }
  .canvas {
    position: relative;
    width: 1200px;
    height: 720px;
    background: var(--page);
    font-family: "Open Sans", "Myriad Pro", Arial, sans-serif;
  }
  .card-back {
    position: absolute;
    left: 71px;
    top: 72px;
    width: 516px;
    height: 570px;
    background: var(--card-dark);
    color: var(--ink-light);
    display: flex;
    flex-direction: column;
    align-items: center;
    justify-content: center;
    text-align: center;
    font-size: 31px;
    line-height: 1.3;
    padding-bottom: 48px;
    box-sizing: border-box;
  }
  .contact-block { margin: 0 0 31px; }
  .contact-block:last-child { margin-bottom: 0; }
  .card-front {
    position: absolute;
    left: 602px;
    top: 72px;
    width: 516px;
    height: 570px;
    overflow: hidden;
  }
  .site-photo {
    position: absolute;
    inset: 0;
    background: linear-gradient(to bottom,
      var(--photo-top) 0%,
      var(--photo-top) 55%,
      var(--photo-mid) 68%,
      var(--photo-low) 80%,
      var(--photo-mid) 100%);
  }
  .name-box {
    position: absolute;
    left: 142px;
    top: 174px;
    width: 221px;
    height: 220px;
    background: var(--name-box);
    color: var(--ink-light);
    display: flex;
    flex-direction: column;
    justify-content: center;
    align-items: center;
    font-weight: 600;
    font-size: 50px;
    line-height: 1.2;
    letter-spacing: 1px;
  }
</style>
</head>
<body>
  <div class="canvas">
    <section class="card-back">
      <p class="contact-block">6127 NE 318th Avenue Suite 241<br>Miami Lakes, FL 33482</p>
      <p class="contact-block">(305) 472-1803</p>
      <p class="contact-block">curtis@quarvinta.com</p>
    </section>
    <section class="card-front">
      <div class="site-photo" role="img" aria-label="Black and white photo of workers pushing wheelbarrows on a concrete building slab supported by scaffolding"></div>
      <div class="name-box">
        <span>CURTIS</span>
        <span>ORTEGA</span>
      </div>
    </section>
  </div>
</body>
</html>
```